Business Card for Modern Marketing Consultancy

Business card needed for marketing consultancy with existing logo.

Lanternway Co is a specialized boutique marketing consultancy that provides startup, small and mid size consumer businesses thought leadership and implementation of marketing strategies to help your business grow.

Our expertise, experience and industry knowledge stems from some of New York’s top global beauty and retail companies and allows us to draw from an array of successful marketing strategies and growth tactics tailored to suit the needs of your business

lanternwayco.example

Target Market(s)

start up, small and mid size consumer packaged goods businesses

Industry/Entity Type

Leadership

Requirements
Must have
• Must have the logo of the business and use of the exact colors of the logo.
Must be simple, sleek, modern and clean. Must make a statement and be eye catching.

Front: looking for unique design or visual statement with logo and tagline

Back of card should have:
logo - if not use on front.
Delia R. Horvath
Founder
Lanternway Co
m: 555.014.2276
deliahorvath@lanternwayco.example
lanternwayco.example

Please use the following words as these describe my services:
strategy analytics branding research

Please refer to the website look and feel: lanternwayco.example

Please kindly note that I am looking for a unique design that I cannot do myself with a template. thank you.
Nice to have
• Please also try and incorporate additional files attached.

```html
<!DOCTYPE html>
<html lang="en">
<head>
<meta charset="UTF-8">
<title>Lanternway Co — Business Card</title>
<link href="https://fonts.googleapis.com/css2?family=Arimo:wght@400;700&family=Oswald:wght@600&display=swap" rel="stylesheet">
<style>
  :root {
    --magenta: #d8137c;
    --magenta-deep: #b80d69;
    --card-white: #ffffff;
    --card-grey: #8f8f8f;
    --panel-grey: #9a9a9a;
    --ink-white: #ffffff;
    --stage: #e6e6e6;
  }
  * { box-sizing: border-box; margin: 0; padding: 0; }
  html, body {
    width: 1200px;
    height: 900px;
    overflow: hidden;
    background: var(--stage);
    font-family: "Arimo", Arial, sans-serif;
  }
  .canvas {
    position: relative;
    width: 1200px;
    height: 900px;
  }
  .card {
    position: absolute;
    left: 280px;
    width: 640px;
    height: 366px;
    border-radius: 4px;
    box-shadow: 0 10px 28px rgba(0,0,0,0.18);
    overflow: hidden;
  }

  /* Front */
  .card-front {
    top: 64px;
    background: var(--card-white);
  }
  .front-mark {
    position: absolute;
    left: 56px;
    top: 118px;
    display: flex;
    align-items: center;
    gap: 18px;
  }
  .front-mark .dot {
    width: 46px;
    height: 46px;
    border-radius: 50%;
    background: var(--magenta);
  }
  .front-mark .name {
    font-size: 58px;
    font-weight: 700;
    color: var(--magenta);
    letter-spacing: -1px;
  }
  .tagline {
    position: absolute;
    right: 40px;
    bottom: 34px;
    font-size: 13px;
    color: var(--magenta);
  }

  /* Back */
  .card-back {
    top: 470px;
    background: var(--card-grey);
  }
  .back-mark {
    position: absolute;
    left: 40px;
    top: 40px;
    display: flex;
    align-items: center;
    gap: 10px;
  }
  .back-mark .name {
    font-size: 34px;
    font-weight: 700;
    color: var(--ink-white);
    letter-spacing: -0.5px;
  }
  .back-mark .dot {
    width: 18px;
    height: 18px;
    border-radius: 50%;
    background: var(--magenta);
  }
  .contact-panel {
    position: absolute;
    left: 300px;
    top: 150px;
    width: 300px;
    height: 62px;
    background: var(--panel-grey);
  }
  .name-band {
    position: absolute;
    left: 260px;
    right: 0;
    top: 128px;
    height: 40px;
    background: var(--magenta);
    display: flex;
    align-items: center;
    padding-left: 24px;
  }
  .name-band h1 {
    font-family: "Oswald", "Arial Narrow", sans-serif;
    font-weight: 600;
    font-size: 24px;
    color: var(--ink-white);
    text-transform: uppercase;
    letter-spacing: 0.5px;
  }
  .details {
    position: absolute;
    left: 284px;
    top: 216px;
    list-style: none;
    color: var(--ink-white);
    font-size: 15px;
    line-height: 26px;
  }
  .details .company { font-size: 17px; margin-bottom: 4px; }
  .details li { display: flex; align-items: center; gap: 10px; }
  .details svg { width: 13px; height: 13px; flex: none; }
  .details .web { color: var(--magenta); padding-left: 23px; font-size: 16px; }
</style>
</head>
<body>
<main class="canvas">
  <section class="card card-front" aria-label="Card front">
    <div class="front-mark">
      <span class="dot"></span>
      <span class="name">Lanternway Co</span>
    </div>
    <p class="tagline">strategy analytics branding research ....</p>
  </section>

  <section class="card card-back" aria-label="Card back">
    <div class="back-mark">
      <span class="name">Lanternway Co</span>
      <span class="dot"></span>
    </div>
    <div class="contact-panel"></div>
    <div class="name-band"><h1>Delia R. Horvath</h1></div>
    <ul class="details">
      <li class="company">Lanternway Co</li>
      <li>
        <svg viewBox="0 0 24 24" aria-hidden="true"><path fill="#d8137c" d="M6.6 10.8a15.1 15.1 0 0 0 6.6 6.6l2.2-2.2c.3-.3.7-.4 1-.2 1.1.4 2.3.6 3.6.6.6 0 1 .4 1 1V20c0 .6-.4 1-1 1A17 17 0 0 1 3 4c0-.6.4-1 1-1h3.5c.6 0 1 .4 1 1 0 1.3.2 2.5.6 3.6.1.3 0 .7-.2 1z"/></svg>
        <span>555.014.2276</span>
      </li>
      <li>
        <svg viewBox="0 0 24 24" aria-hidden="true"><rect x="2" y="5" width="20" height="14" rx="2" fill="#d8137c"/><path d="M3 6l9 7 9-7" stroke="#8f8f8f" stroke-width="2" fill="none"/></svg>
        <span>deliahorvath@lanternwayco.example</span>
      </li>
      <li class="web">lanternwayco.example</li>
    </ul>
  </section>
</main>
</body>
</html>
```